Expanding the consciousness of Humanity - Solvane-Harbor

Please note that whoever will win this project , a 1on1 Powerpoint design project will separately be launched and will be offered to the winning designer.

---------
This letterhead is to provide proposals, as well as manuals for my clients.

I am looking for the letter, power point design and business card that inspires people when they see it, that they feel that design has been done with love and passion. Something that is professional, simple and yet creative, Business like, yet spiritual. That inspires growth!

This part of the branding for my company, therefore the business card as well as the power point design that will come after as 1on1 project should have the same team and feeling.

Solvane harbor, The company will be providing Coaching services (one-one or groups) to corporations, teams and individuals, partnering with them to achieve their goals/vision, by helping them to remove the self-imposed limiting beliefs, helping them to get them out of their own way, helping them to raise their level of consciousness and self-awareness.

The vision is: Bring conscious leadership to the workplace and to individuals for the wellbeing of humanity.

I know that somewhere out there will resonate with this, and will be inspired to provide the best design :) thank you very much!!!!!

MPORTANT:
- To use Free Fonts - let me know where I can download them
- Editable formats please for the double sized business card

LOGO is attached in pdf. If needed other file type please let me know

Thank you thank you in advance for your time and inspiration!! Sending good vibes for a great design out there

Must Have:
- Please keep on mind that the cards - power point will have the same feeling - Corporate branding
- that is not to heavy to look at it, that is simple and beautiful and inspiring
- Looking to have Calibri or Calibri light font

imple, yet inspirational - Professional, yet playful - business like, yet spiritual

I am looking for something different that the "standard" designs out there.

For example, the Logo of the company in the back side with a quote and the front side something simple, yet inspiring. that has the contact info as well as the social media details LinkedIn - Facebook - tweeter - website

Open for suggestions and inspiration :)

Thank you!

Font styles to use
Sans Serif

Requirements
Must have
• - Please keep on mind that the cards - power point will have the same feeling
• - Corporate branding
• - that is not to heavy to look at it, that is simple and beautiful and inspiring
• - Looking to have Calibri or Calibri light font
• - Corporate colours as the logo

```html
<!DOCTYPE html>
<html lang="en">
<head>
<meta charset="utf-8">
<title>Solvane-Harbor Stationery</title>
<link rel="stylesheet" href="https://fonts.googleapis.com/css2?family=Carlito:wght@400;700&display=swap">
<style>
  :root {
    --blue: #1f4a93;
    --gold: #f2b325;
    --ink: #2b2b2b;
    --paper: #fbfbfb;
    --scene: #ececec;
    --faint: #e9eaee;
  }
  * { box-sizing: border-box; margin: 0; padding: 0; }
  html, body { width: 1200px; height: 795px; overflow: hidden; }
  body { background: var(--scene); font-family: "Carlito", "Calibri", sans-serif; color: var(--ink); position: relative; }

  .sheet { position: absolute; background: var(--paper); box-shadow: 0 2px 10px rgba(0,0,0,.12); overflow: hidden; }

  /* Wordmark: plain name beside one plain circle */
  .brand { display: flex; align-items: center; gap: 8px; position: relative; z-index: 1; }
  .brand-dot { width: 22px; height: 22px; border-radius: 50%; background: var(--blue); flex: none; }
  .brand-name { font-weight: 700; color: var(--blue); font-size: 16px; line-height: 1; }

  .contact { font-size: 8px; color: var(--blue); line-height: 1.6; position: relative; z-index: 1; }
  .contact li { list-style: none; display: flex; align-items: center; gap: 4px; }
  .contact svg { width: 8px; height: 8px; flex: none; }

  .halo { position: absolute; border-radius: 50%; background: var(--faint); }

  /* Letterhead */
  .letterhead { left: 40px; top: 28px; width: 523px; height: 740px; }
  .letterhead .brand { position: absolute; left: 44px; top: 56px; }
  .letterhead .contact { position: absolute; right: 60px; top: 42px; }
  .letterhead .halo { width: 150px; height: 150px; right: 70px; top: 78px; }
  .recipient { position: absolute; left: 44px; top: 190px; font-size: 10px; line-height: 1.3; font-style: normal; }
  .recipient strong { font-size: 11px; }
  .letter-body { position: absolute; left: 44px; right: 48px; top: 250px; font-size: 9.6px; line-height: 1.5; }
  .letter-body p + p { margin-top: 12px; }
  .sign-off { position: absolute; left: 44px; top: 470px; font-size: 9.6px; line-height: 1.35; }
  .signature { display: block; width: 140px; height: 40px; margin: 6px 0 4px; background: linear-gradient(90deg, #d9d9d9, #f0f0f0); border-radius: 4px; }
  .letter-web { position: absolute; right: 44px; bottom: 74px; font-size: 9px; color: var(--blue); }
  .footer-bands { position: absolute; left: 0; right: 0; bottom: 40px; }
  .band-gold { height: 1.5px; background: var(--gold); }
  .band-blue { height: 8px; background: var(--blue); margin: 3px 0; }

  /* Cards */
  .card { width: 300px; height: 171px; }
  .card .halo { width: 100px; height: 100px; }
  .card .footer-bands { bottom: 22px; }
  .card .band-blue { height: 5px; margin: 2px 0; }
  .card .brand-name { font-size: 12px; }
  .card .brand-dot { width: 18px; height: 18px; }

  .card-front { left: 620px; top: 150px; }
  .card-front .halo { right: 18px; top: 8px; }
  .card-front .brand { position: absolute; left: 20px; top: 24px; }
  .holder { position: absolute; left: 20px; top: 70px; color: var(--blue); }
  .holder-name { font-weight: 700; font-size: 11px; text-transform: uppercase; }
  .holder-role { font-size: 7px; color: var(--gold); margin-bottom: 5px; }
  .card-front .contact { font-size: 7.5px; }
  .card-web { position: absolute; right: 20px; top: 110px; font-size: 7.5px; color: var(--blue); }

  .card-back { left: 620px; top: 370px; }
  .card-back .halo { left: 20px; top: 20px; }
  .card-back .brand { position: absolute; left: 140px; top: 54px; }
  .card-line { position: absolute; left: 0; right: 0; top: 100px; text-align: center; font-size: 8px; color: var(--blue); position: absolute; z-index: 1; }
</style>
</head>
<body>

  <section class="sheet letterhead">
    <div class="halo" aria-hidden="true"></div>
    <div class="brand">
      <span class="brand-dot"></span>
      <span class="brand-name">Solvane-Harbor</span>
    </div>
    <ul class="contact">
      <li><svg viewBox="0 0 10 10"><circle cx="5" cy="5" r="5" fill="#f2b325"/><path d="M3 2.5l1 1-.6.8c.4.8 1 1.4 1.8 1.8l.8-.6 1 1-.6 1C4.5 7.5 2.5 5.5 2.5 3.1z" fill="#fff"/></svg>+1 555 014 2290</li>
      <li><svg viewBox="0 0 10 10"><circle cx="5" cy="5" r="5" fill="#f2b325"/><rect x="2.5" y="3.2" width="5" height="3.6" fill="none" stroke="#fff" stroke-width=".8"/><path d="M2.5 3.2L5 5.3l2.5-2.1" fill="none" stroke="#fff" stroke-width=".8"/></svg>hello@solvaneharbor.com</li>
    </ul>

    <address class="recipient">
      <strong>ELIAS MARREN</strong><br>
      14 Lumen Row, Aldergate<br>
      20418
    </address>

    <div class="letter-body">
      <p>Lorem Ipsum is simply dummy text of the printing and typesetting industry. Lorem Ipsum has been the industry's standard dummy text ever since the 1500s, when an unknown printer took a galley of type and scrambled it to make a type specimen book. It has survived not only five centuries, but also the leap into electronic typesetting, remaining essentially unchanged. It was popularised in the 1960s with the release of Letraset sheets containing Lorem Ipsum passages, and more recently with desktop publishing software like Aldus PageMaker including versions of Lorem Ipsum.</p>
      <p>It is a long established fact that a reader will be distracted by the readable content of a page when looking at its layout. The point of using Lorem Ipsum is that it has a more-or-less normal distribution of letters, as opposed to using 'Content here, content here', making it look like readable English. Many desktop and all years, sometimes by accident, sometimes on purpose (injected humour and the like).</p>
    </div>

    <div class="sign-off">
      Regards,
      <span class="signature" role="img" aria-label="Handwritten signature of Elias Marren"></span>
      Elias Marren<br>
      General Manager
    </div>

    <div class="letter-web">www.solvaneharbor.com</div>
    <div class="footer-bands" aria-hidden="true">
      <div class="band-gold"></div><div class="band-blue"></div><div class="band-gold"></div>
    </div>
  </section>

  <section class="sheet card card-front">
    <div class="halo" aria-hidden="true"></div>
    <div class="brand">
      <span class="brand-dot"></span>
      <span class="brand-name">Solvane-Harbor</span>
    </div>
    <div class="holder">
      <div class="holder-name">Noor Vell</div>
      <div class="holder-role">Founder</div>
      <ul class="contact">
        <li><svg viewBox="0 0 10 10"><circle cx="5" cy="5" r="5" fill="#f2b325"/><path d="M3 2.5l1 1-.6.8c.4.8 1 1.4 1.8 1.8l.8-.6 1 1-.6 1C4.5 7.5 2.5 5.5 2.5 3.1z" fill="#fff"/></svg>+1 555 014 2290</li>
        <li><svg viewBox="0 0 10 10"><circle cx="5" cy="5" r="5" fill="#f2b325"/><rect x="2.5" y="3.2" width="5" height="3.6" fill="none" stroke="#fff" stroke-width=".8"/><path d="M2.5 3.2L5 5.3l2.5-2.1" fill="none" stroke="#fff" stroke-width=".8"/></svg>hello@solvaneharbor.com</li>
      </ul>
    </div>
    <div class="card-web">www.solvaneharbor.com</div>
    <div class="footer-bands" aria-hidden="true">
      <div class="band-gold"></div><div class="band-blue"></div><div class="band-gold"></div>
    </div>
  </section>

  <section class="sheet card card-back">
    <div class="halo" aria-hidden="true"></div>
    <div class="brand">
      <span class="brand-dot"></span>
      <span class="brand-name">Solvane-Harbor</span>
    </div>
    <div class="card-line">Solvane harbor &amp; Corporate Conscious Leadership Coaching</div>
    <div class="footer-bands" aria-hidden="true">
      <div class="band-gold"></div><div class="band-blue"></div><div class="band-gold"></div>
    </div>
  </section>

</body>
</html>
```